MEDITERRANEAN Cafe Website needed

We are a MEDITERRANEAN Café serving Coffee, breakfast, Pizza, Pasta, Sandwiches etc.

We need a home page, menu & venue, Reservations & Events, Delivery
Connect (Social media / Feedback / Contact us),Join our team
Updates

Can we keep the designs in Mediterranean colours, look, and feel pleasethanks Added Saturday, December 10, 2016

Project Deadline Extended Reason: I have guarantied the payment and upgraded the project. I would like this would to give more time for new designs to come in and a couple of potential designs to show more. Added Sunday, December 11, 2016

Industry/Entity Type

Cafe

Coding

Coded - Design and coding required

Number of Pages Required

5+ page

Requirements
Must have
• MEDITERRANEAN feel, colours, style etc.
• http://www.quillandfen (DOT) co (DOT) uk
Nice to have

```html
<!DOCTYPE html>
<html lang="en">
<head>
<meta charset="utf-8">
<title>Olivera Café – Home</title>
<link rel="stylesheet" href="https://fonts.googleapis.com/css2?family=Open+Sans:wght@400;600;700&family=Source+Sans+3:wght@300;400;600&display=swap">
<style>
:root{
  --red:#c8161d;
  --red-dark:#a51016;
  --maroon:#5a1a1c;
  --wine:#7a2326;
  --ink:#1b1b1b;
  --text:#333;
  --white:#fff;
  --footer:#1e1e1e;
  --footer-bar:#111;
  --field:#000;
}
*{box-sizing:border-box;margin:0;padding:0}
html,body{width:1200px;height:5056px;overflow:hidden;background:#fff}
body{font-family:"Open Sans",sans-serif;color:var(--text);position:relative}
section,header,footer,nav{position:absolute;left:0;width:1200px}
.abs{position:absolute}
.heading{font-family:"Source Sans 3",sans-serif;font-weight:400;color:var(--ink);text-align:center;width:100%;font-size:72px;line-height:1}
.subheading{font-family:"Source Sans 3",sans-serif;font-weight:300;text-align:center;width:100%;font-size:32px;letter-spacing:1px}
.body-copy{font-size:13px;line-height:22px;text-align:center}
.read-more{font-size:13px;color:var(--red);text-align:center;width:100%;font-weight:600}
.read-more svg{vertical-align:middle;margin:0 8px}

/* hero */
.hero{top:0;height:792px;background:linear-gradient(160deg,#8a7b6e 0%,#b79a7a 30%,#c0512d 55%,#6f6359 80%,#9b9085 100%)}
.hero-search{left:68px;top:712px;width:290px;height:30px;border:2px solid #fff;color:#fff;font-size:11px;font-weight:700;padding:5px 12px;letter-spacing:.5px}
.hero-search svg{position:absolute;right:12px;top:6px}
.slider-dots{left:490px;top:718px;display:flex;gap:22px}
.slider-dots span{width:18px;height:18px;border-radius:50%;background:#111}
.slider-dots span:first-child{background:#fff}
.hero-btn{top:714px;height:28px;border:2px solid #fff;color:#fff;font-size:11px;font-weight:700;padding:5px 14px;letter-spacing:.5px}

/* nav band */
.nav-band{top:792px;height:152px;background:var(--red)}
.social-row{left:340px;top:22px;width:520px;height:64px}
.social-row .line{position:absolute;top:31px;left:40px;right:40px;height:2px;background:#fff}
.social-row .dot{position:absolute;top:0;width:64px;height:64px;border-radius:50%;border:3px solid #fff;background:var(--red)}
.main-nav{top:112px;left:0;width:1200px;display:flex;justify-content:center;gap:48px;font-size:14px;color:#fff}
.main-nav .active{color:#ffd23c}

/* story */
.story{top:944px;height:876px}
.brand{left:0;top:160px;width:100%;text-align:center;font-family:"Source Sans 3",sans-serif;font-weight:600;color:var(--red);font-size:84px;line-height:1}
.brand small{display:block;font-size:22px;letter-spacing:4px;margin-top:8px}
.story .heading{top:476px}

/* menus */
.menus{top:1820px;height:640px;background:linear-gradient(180deg,rgba(90,26,28,.92),rgba(120,40,38,.85)),linear-gradient(120deg,#5c3a2c,#a4654a 50%,#4a2a22)}
.menu-card{top:192px;width:283px;height:374px;border:2px solid #fff;color:#fff;text-align:center}
.menu-badge{top:-115px;left:57px;width:168px;height:168px;border-radius:50%;display:flex;flex-direction:column;align-items:center;justify-content:center;font-size:20px;font-weight:700;font-family:"Source Sans 3",sans-serif}
.menu-badge.red{background:var(--red)}
.menu-badge.muted{background:#8a5149}
.menu-price{position:absolute;top:148px;width:100%;font-family:"Source Sans 3",sans-serif;font-size:26px;font-weight:600;line-height:1.1}
.menu-price b{font-size:40px;font-weight:400}
.menu-link{position:absolute;bottom:28px;width:100%;font-size:12px}

/* team */
.team{top:2460px;height:782px}
.team .heading{top:112px}
.portrait{top:422px;width:210px;height:210px;border-radius:50%;border:4px solid #eee;background:radial-gradient(circle at 50% 40%,#d9c3b0,#9d8a7a 70%,#e8e8e8)}
.member{top:670px;width:300px;text-align:center;font-size:14px;font-weight:700;color:var(--red);letter-spacing:.5px}
.arrow{top:522px}

/* reserve */
.reserve{top:3242px;height:448px;background:linear-gradient(180deg,#4a1518,#6e2124 60%,#5a1a1c)}
.reserve .heading{top:62px;color:#fff}
.reserve .subheading{top:138px;color:#fff}
.field{height:42px;border:2px solid #ddd;border-radius:4px;color:#fff;font-size:12px;padding:10px 12px;background:rgba(0,0,0,.08)}
.btn-red{background:var(--red);color:#fff;font-size:12px;font-weight:700;border-radius:4px;display:flex;align-items:center;justify-content:center;gap:10px}

/* events */
.events{top:3690px;height:887px}
.events .heading{top:118px}
.events .subheading{top:198px;color:var(--text)}
.event-photo{left:135px;top:320px;width:478px;height:310px;background:linear-gradient(135deg,#c9b6a0,#b5322b 45%,#e3d3bf 75%,#8a7766)}
.event-point{left:674px;width:400px;font-size:14px;line-height:22px}
.event-point::before{content:"";position:absolute;left:0;top:3px;width:16px;height:16px;border-radius:50%;background:var(--red)}
.event-point p{margin-left:32px}

/* footer */
.site-footer{top:4577px;height:428px;background:var(--footer);color:#fff}
.footer-title{font-family:"Source Sans 3",sans-serif;font-size:30px;font-weight:600}
.footer-copy{font-size:12px;line-height:20px;color:#ccc}
.f-field{left:763px;width:302px;height:46px;background:var(--field);font-size:12px;padding:14px 12px;color:#ddd}
.plain-social{width:30px;height:30px;border-radius:50%;background:#fff}
.bottom-bar{top:5005px;height:51px;background:var(--footer-bar);color:#fff;font-size:12px;font-weight:700;text-align:center;line-height:51px}
</style>
</head>
<body>

<header class="hero" role="img" aria-label="Overhead photograph of a pizza with tomatoes, olives, mushrooms and basil on a rustic wooden table">
  <div class="abs hero-search">SEARCH FOOD
    <svg width="18" height="18" viewBox="0 0 18 18"><circle cx="7" cy="7" r="5" fill="none" stroke="#fff" stroke-width="2"/><line x1="11" y1="11" x2="16" y2="16" stroke="#fff" stroke-width="2"/></svg>
  </div>
  <div class="abs slider-dots"><span></span><span></span><span></span><span></span><span></span></div>
  <div class="abs hero-btn" style="left:892px">JOIN NOW</div>
  <div class="abs hero-btn" style="left:1010px">RESERVATIONS</div>
</header>

<nav class="nav-band">
  <div class="abs social-row">
    <div class="line"></div>
    <div class="dot" style="left:0"></div>
    <div class="dot" style="left:152px"></div>
    <div class="dot" style="left:304px"></div>
    <div class="dot" style="left:456px"></div>
  </div>
  <div class="abs main-nav">
    <span class="active">Home</span><span>About US</span><span>Our Story</span><span>Our Team</span><span>Menu</span><span>Events</span><span>Contact us</span>
  </div>
</nav>

<section class="story">
  <div class="abs brand">Olivera<small>WRAPS &amp; GRILL</small></div>
  <h1 class="abs heading">Our Story</h1>
  <p class="abs body-copy" style="left:135px;top:620px;width:930px">An early morning walk to the bakery around the corner is a way of life in the Mediterranean. Nothing beats the first batch of bread from the oven to start your day. Olivera Café started with a simple idea, “we wanted people to experience that taste all the time”. So we combined a variety of best ingredients and delicacies to make you that healthy stuffed all fresh Pitta to enjoy the way you like and whenever you got the urge to do so.<br>As time went by we opened our hearts and ears to our customers and added a range of fresh and delicious products to our menu – salads, traditional Mediterranean starters, desserts and we made sure you don't miss out on the great morning Lattes.</p>
  <p class="abs read-more" style="top:770px">
    <svg width="16" height="14" viewBox="0 0 16 14"><path d="M2 12 L8 3 L10 8 Z" fill="#333"/></svg>Read More<svg width="16" height="14" viewBox="0 0 16 14"><path d="M2 12 L13 2 M9 2 L13 2 L13 6" stroke="#333" stroke-width="2" fill="none"/></svg>
  </p>
</section>

<section class="menus" role="img" aria-label="Dimmed photograph of plated dishes on a restaurant table under a red tint">
  <div class="abs menu-card" style="left:135px">
    <div class="abs menu-badge red">BREAKFAST</div>
    <div class="menu-price">FROM<br><b>£4.75</b></div>
    <div class="menu-link">View Menu</div>
  </div>
  <div class="abs menu-card" style="left:458px">
    <div class="abs menu-badge muted">LUNCH<svg width="22" height="22" viewBox="0 0 22 22" style="margin-top:8px"><path d="M6 2v8M4 2v5a2 2 0 0 0 4 0V2M6 10v10M15 2c-3 0-3 8 0 9v9" stroke="#fff" stroke-width="2" fill="none"/></svg></div>
    <div class="menu-price">FROM<br><b>£6.95</b></div>
    <div class="menu-link">View Menu</div>
  </div>
  <div class="abs menu-card" style="left:782px">
    <div class="abs menu-badge red">MAIN MENU</div>
    <div class="menu-price" style="font-size:20px;font-weight:700;line-height:1.9">ENJOY THE TASTE<br>OF ITALY</div>
    <div class="menu-link">View Menu</div>
  </div>
</section>

<section class="team">
  <h2 class="abs heading">Our Team</h2>
  <p class="abs body-copy" style="left:135px;top:236px;width:930px">One of the centrepieces and the Mediterranean symbol of Olivera Café are its colors which inspire a carefree ease, and invitation to relax in that particular world of Olivera Café. The mixture of captivating marina view and fresh ingredients is played in perfect harmony with the restaurant's atmosphere.<br>Our team has a great sense of pride in everything we do and a passion to ensure you have an incredible experience every time.</p>
  <p class="abs read-more" style="top:330px">Read More</p>
  <svg class="abs arrow" style="left:26px" width="26" height="40" viewBox="0 0 26 40"><path d="M20 4 L6 20 L20 36" stroke="#111" stroke-width="6" fill="none"/></svg>
  <svg class="abs arrow" style="left:1148px" width="26" height="40" viewBox="0 0 26 40"><path d="M6 4 L20 20 L6 36" stroke="#111" stroke-width="6" fill="none"/></svg>
  <div class="abs portrait" style="left:138px" role="img" aria-label="Portrait of team member Dan Morrow"></div>
  <div class="abs portrait" style="left:495px" role="img" aria-label="Portrait of team member Theo Castell"></div>
  <div class="abs portrait" style="left:852px" role="img" aria-label="Portrait of team member Nina Rowe"></div>
  <div class="abs member" style="left:93px">DAN MORROW</div>
  <div class="abs member" style="left:450px">THEO CASTELL</div>
  <div class="abs member" style="left:807px">NINA ROWE</div>
</section>

<section class="reserve">
  <h2 class="abs heading">Reserve Now</h2>
  <p class="abs subheading">EVERY GUEST IS SPECIAL HERE</p>
  <div class="abs field" style="left:135px;top:260px;width:253px">Name</div>
  <div class="abs field" style="left:478px;top:260px;width:246px">Date</div>
  <div class="abs field" style="left:816px;top:260px;width:249px">Person</div>
  <div class="abs field" style="left:135px;top:324px;width:253px">E-Mail</div>
  <div class="abs field" style="left:478px;top:324px;width:246px">Time</div>
  <div class="abs btn-red" style="left:816px;top:324px;width:249px;height:42px">MAKE A Reservations</div>
</section>

<section class="events">
  <h2 class="abs heading">Events</h2>
  <p class="abs subheading">JOIN US FOR SOMETHING SPECIAL</p>
  <div class="abs event-photo" role="img" aria-label="Photograph of a child in a red jacket eating pizza at a café table"></div>
  <div class="abs event-point" style="top:317px"><p>All of your Olivera Café favorites are available, just right, easily and affordable.</p></div>
  <div class="abs event-point" style="top:401px"><p>Turn any large party or event into a Olivera Café celebration.</p></div>
  <div class="abs event-point" style="top:499px"><p>We will gladly honor requests to modify orders to suit specific health or dietary needs.</p></div>
  <div class="abs btn-red" style="left:878px;top:600px;width:187px;height:34px;border-radius:0">SEE ALL EVENTS</div>
  <p class="abs body-copy" style="left:135px;top:686px;width:930px">Be it an intimate gathering of friends, a celebration of a corporate milestone, or an engagement reception, Olivera Café is the perfect venue. Reserve with us and let us be your host to a true event.</p>
  <p class="abs read-more" style="top:756px">Read More</p>
</section>

<footer class="site-footer">
  <h3 class="abs footer-title" style="left:135px;top:50px">Location</h3>
  <p class="abs footer-copy" style="left:135px;top:120px;width:480px">Located in Harbour Quay, Olivera Café has become a beacon for Service and Quality food. Enjoy an after-dinner coffee or drink from the spacious waterfront magical outdoors of the Marina or our comfortable indoor where you can relax and spend a memorable time with us.</p>
  <h3 class="abs footer-title" style="left:135px;top:250px">Social media</h3>
  <div class="abs plain-social" style="left:135px;top:326px"></div>
  <div class="abs plain-social" style="left:180px;top:326px"></div>
  <div class="abs plain-social" style="left:225px;top:326px"></div>
  <div class="abs plain-social" style="left:270px;top:326px"></div>
  <div class="abs plain-social" style="left:315px;top:326px"></div>
  <div class="abs plain-social" style="left:360px;top:326px"></div>
  <h3 class="abs footer-title" style="left:763px;top:50px">Contact us</h3>
  <div class="abs f-field" style="top:123px">Name</div>
  <div class="abs f-field" style="top:190px">Your Mail</div>
  <div class="abs f-field" style="top:257px">Message</div>
  <div class="abs btn-red" style="left:763px;top:323px;width:150px;height:40px;border-radius:0">SUBMIT</div>
</footer>

<div class="abs bottom-bar" style="left:0;width:1200px">© 2016 | ALL RIGHTS RESERVED</div>

</body>
</html>
```